3 x Professional Herbal Supplement Label Design Ready to Print in UK Standard + Example inc

Hi,
Thank you for taking the time to read. I'm looking for an excellent graphic designer experienced in creating supplement labels for our 3 new products. The labels should be sized and have the resolution ready for the printers.
Here is the work:
I'm looking for a new supplement label design that I can use for 3 new products called:
1 - Raspberry Ketone
2 - Garcinia Cambogia
3 - Green Coffee
You will only need to create a single label to enter the competition, as the label created will be the template for all 3 products listed above. You can choose whether you go for product 1, 2,or 3 to enter the design competition, but all 3 will be required on completion should you be selected.
Simply, the label template would be adjusted for the other products, what would be different is the product specifics like, name, background graphic of the ingredient and ingredients listed, directions of use, barcode etc.
The design I like, which I'd like you to copy and then artistically make different is attached and titled "BrightMeadow_Garcinia_Cambogia_LABEL.jpg"
My company logo is attached called "vorix final logo.ai" & "vorix-invis.png" - Please let me know if this resolution is not suitable.
The guidance information in designing a UK label from the supplement manufacturer is attached, as follows:
The supplement manufacturer has also provided a very basic example of a product they produced for another company (Not very good I know, but at least shows what goes where). Please do not use this as an example of a good design!
*** I will provide more specific product detail (ingredients, bar-code, dosage) if your initial design is liked and selected for adjustment, as we will require that all 3 label designs are completed.
*** The delivered image files will need to be in Photoshop format.

```html
<!DOCTYPE html>
<html lang="en">
<head>
<meta charset="utf-8">
<title>Green Coffee Supplement Label</title>
<link href="https://fonts.googleapis.com/css2?family=Arimo:wght@400;700&family=Playfair+Display:wght@400&display=swap" rel="stylesheet">
<style>
  :root {
    --page-bg: #ececec;
    --label-green: #2f7a13;
    --badge-green: #97c54a;
    --accent-lime: #a8d34b;
    --ink-dark-green: #2c7412;
    --white: #ffffff;
    --bean-light: #8a9a3a;
    --bean-dark: #4d5a1c;
    --sack: #9c7a4e;
  }
  * { margin: 0; padding: 0; box-sizing: border-box; }
  html, body { width: 1200px; height: 541px; overflow: hidden; background: var(--page-bg); }
  body { position: relative; font-family: "Arimo", Arial, sans-serif; }
  h1, h2, h3 { font-size: inherit; font-weight: inherit; }

  .label {
    position: absolute; left: 110px; top: 93px; width: 980px; height: 354px;
    background: var(--label-green); overflow: hidden;
  }
  .panel-left { position: absolute; left: 40px; top: 52px; width: 200px; color: var(--white); }
  .section-heading { color: var(--accent-lime); font-weight: 700; font-size: 10.5px; line-height: 12px; letter-spacing: 0.2px; }
  .usage-text p { font-size: 10px; line-height: 16px; letter-spacing: 0.15px; white-space: nowrap; }
  .caution { margin-top: 16px; }
  .caution-text p { font-size: 10px; line-height: 14.4px; letter-spacing: 0.15px; white-space: nowrap; }

  .brand { display: flex; align-items: center; gap: 6px; color: var(--white); font-weight: 400; }
  .brand-dot { width: 14px; height: 14px; border-radius: 50%; background: currentColor; }
  .brand-left { position: absolute; left: 108px; top: 285px; font-size: 23px; line-height: 26px; }
  .brand-right { position: absolute; left: 762px; top: 75px; font-size: 22px; line-height: 26px; }

  .bean-photo { position: absolute; border-radius: 50% 45% 40% 50%; }
  .bean-photo.left {
    left: 235px; top: 150px; width: 165px; height: 170px;
    background: radial-gradient(ellipse at 60% 30%, var(--sack) 0%, var(--bean-light) 40%, var(--bean-dark) 75%, rgba(47,122,19,0) 100%);
  }
  .bean-photo.right {
    left: 590px; top: 150px; width: 165px; height: 170px;
    background: radial-gradient(ellipse at 40% 30%, var(--sack) 0%, var(--bean-light) 40%, var(--bean-dark) 75%, rgba(47,122,19,0) 100%);
  }

  .badge { position: absolute; left: 384px; top: 12px; width: 192px; height: 318px; }
  .badge svg { position: absolute; left: 0; top: 0; }
  .badge-content { position: absolute; left: 0; top: 0; width: 192px; height: 318px; text-align: center; color: var(--ink-dark-green); }
  .badge-brand { position: absolute; top: 77px; left: 0; width: 100%; justify-content: center; font-size: 16px; line-height: 20px; }
  .badge-brand .brand-dot { width: 10px; height: 10px; }
  .product-name {
    position: absolute; top: 103px; left: 0; width: 100%;
    font-family: "Playfair Display", Georgia, serif; font-size: 48px; line-height: 44px;
    transform: scaleX(0.8); letter-spacing: 0.5px; white-space: nowrap;
  }
  .capsule-count { position: absolute; top: 207px; left: 0; width: 100%; font-size: 5.5px; color: var(--white); letter-spacing: 0.3px; }
  .claims { position: absolute; top: 223px; left: 0; width: 100%; font-size: 9.5px; line-height: 13.5px; font-weight: 700; color: var(--ink-dark-green); }
  .claims .headline { letter-spacing: 0.3px; }

  .panel-right { position: absolute; left: 762px; top: 112px; color: var(--white); font-size: 11px; }
  .facts-title { font-weight: 700; font-size: 11px; line-height: 13px; }
  .facts-serving { font-size: 11px; line-height: 14px; }
  .ingredients-title { font-weight: 700; font-size: 11px; margin-top: 13px; line-height: 14px; }
  .ingredient-list { list-style: none; margin-top: 8px; font-size: 10.5px; line-height: 15px; letter-spacing: 0.2px; }
</style>
</head>
<body>
  <main class="label">
    <section class="panel-left">
      <h2 class="section-heading">SUGGESTED USE</h2>
      <div class="usage-text">
        <p>details will be placed here details will be</p>
        <p>placed here details will be placed here</p>
        <p>details will be placed here details will be</p>
        <p>placed here details will be placed here</p>
      </div>
      <div class="caution">
        <h2 class="section-heading">CAUTION</h2>
        <div class="caution-text">
          <p>details will be placed here details will be</p>
          <p>placed here details will be placed here</p>
          <p>details will be placed here details will be</p>
          <p>placed here details will be placed here</p>
          <p>details will be placed here details will be</p>
          <p>placed here details will be placed here</p>
          <p>details will be placed here details will be</p>
          <p>placed here details will be placed here</p>
          <p>details will be placed here details will be</p>
        </div>
      </div>
    </section>
    <div class="brand brand-left"><span class="brand-dot"></span>vorix</div>

    <div class="bean-photo left" role="img" aria-label="Burlap sack spilling green coffee beans"></div>
    <div class="bean-photo right" role="img" aria-label="Burlap sack spilling green coffee beans"></div>

    <div class="badge">
      <svg width="192" height="318" viewBox="0 0 192 318">
        <path fill="#ffffff" d="M0 58 Q0 41 17 41 H33 Q53 41 53 21 Q53 0 74 0 H118 Q139 0 139 21 Q139 41 159 41 H175 Q192 41 192 58 V260 Q192 277 175 277 H159 Q139 277 139 297 Q139 318 118 318 H74 Q53 318 53 297 Q53 277 33 277 H17 Q0 277 0 260 Z"/>
        <path fill="#97c54a" d="M9 60 Q9 50 19 50 H36 Q62 50 62 24 Q62 9 77 9 H115 Q130 9 130 24 Q130 50 156 50 H173 Q183 50 183 60 V258 Q183 268 173 268 H156 Q130 268 130 294 Q130 309 115 309 H77 Q62 309 62 294 Q62 268 36 268 H19 Q9 268 9 258 Z"/>
      </svg>
      <div class="badge-content">
        <div class="brand badge-brand"><span class="brand-dot"></span>vorix</div>
        <h1 class="product-name">GREEN<br>COFFEE</h1>
        <p class="capsule-count">120 VEGETERIAN CAPSULES</p>
        <div class="claims">
          <p class="headline">50% CHLOROGENIC ACID</p>
          <p>Advanced Formula</p>
          <p>Maximum Strength</p>
        </div>
      </div>
    </div>

    <div class="brand brand-right"><span class="brand-dot"></span>vorix</div>
    <section class="panel-right">
      <h2 class="facts-title">Supplement Facts</h2>
      <p class="facts-serving">Serving Size 2 Capsules</p>
      <h3 class="ingredients-title">Ingredients Per Serving</h3>
      <ul class="ingredient-list">
        <li>400mg GREEN COFFEE BEAN</li>
        <li>12:1 EXTRACT 50%</li>
        <li>CHLOROGENIC ACID</li>
        <li>400mg GREEN TEA P.E</li>
        <li>95% Polyphenols</li>
        <li>200mg CAFFEINE Anhydrous</li>
      </ul>
    </section>
  </main>
</body>
</html>
```